Need Business Card for our Indian Grocery Store

Industry/Entity Type

Grocery Store

Contact Information for Business Card

Manoj Baweja
Director

Store Locations:

Eastbrook
482 Elm Parade
P: 03 9172 5843

Northvale
613 Carlow Road
P: 03 9238 6014

email: kvtmarts@mailnest.example

Requirements
Must have
• Our logo Colours

```html
<!DOCTYPE html>
<html lang="en">
<head>
<meta charset="utf-8">
<title>KVT Marts – Business Card</title>
<link rel="stylesheet" href="https://fonts.googleapis.com/css2?family=EB+Garamond:wght@400;500&display=swap">
<style>
  :root {
    --charcoal: #333333;
    --red: #e2140a;
    --white: #ffffff;
    --page: #ffffff;
    --serif: "EB Garamond", Garamond, Georgia, serif;
  }
  * { margin: 0; padding: 0; box-sizing: border-box; }
  html, body { width: 1200px; height: 720px; overflow: hidden; background: var(--page); }
  .canvas { position: relative; width: 1200px; height: 720px; font-family: var(--serif); color: var(--white); }

  .card { position: absolute; top: 159px; width: 578px; height: 400px; overflow: hidden; }
  .card--front { left: 14px; background: var(--charcoal); }
  .card--back { left: 606px; background: var(--red); }

  .corner { position: absolute; width: 64px; height: 89px; }
  .corner--top-left { left: 0; top: 0; }
  .corner--bottom-right { right: 0; bottom: 0; }
  .card--front .corner { background: var(--red); }
  .card--back .corner { background: var(--charcoal); }

  /* Front */
  .brand { position: absolute; left: 0; right: 0; top: 72px; display: flex; justify-content: center; align-items: center; gap: 16px; }
  .brand__square { width: 22px; height: 22px; background: var(--red); }
  .brand__name { font-size: 66px; font-weight: 500; line-height: 1; letter-spacing: 1px; color: var(--white); }

  .person { position: absolute; left: 0; right: 0; top: 249px; text-align: center; font-size: 58px; line-height: 60px; }

  /* Back */
  .locations-title { position: absolute; left: 0; right: 0; top: 37px; text-align: center; font-size: 24px; font-weight: 400; letter-spacing: 0.6px; }
  .store { position: absolute; top: 131px; font-size: 25px; line-height: 36px; white-space: nowrap; }
  .store--north { left: 40px; }
  .store--east { left: 358px; }
  .divider { position: absolute; left: 239px; top: 111px; width: 101px; height: 180px; display: flex; }
  .divider__dark { flex: 1; background: var(--charcoal); }
  .divider__light { flex: 1; background: var(--white); }
  .email { position: absolute; left: 0; right: 0; top: 321px; text-align: center; font-size: 25px; }
</style>
</head>
<body>
<main class="canvas">
  <section class="card card--front" aria-label="Card front">
    <div class="corner corner--top-left"></div>
    <div class="corner corner--bottom-right"></div>
    <div class="brand">
      <span class="brand__square"></span>
      <span class="brand__name">KVT Marts</span>
    </div>
    <p class="person">Manoj Baweja<br>Director</p>
  </section>

  <section class="card card--back" aria-label="Card back">
    <div class="corner corner--top-left"></div>
    <div class="corner corner--bottom-right"></div>
    <h2 class="locations-title">STORE LOCATIONS</h2>
    <p class="store store--north">Northvale<br>613 Carlow Road<br>P: 03 9238 6014</p>
    <div class="divider"><span class="divider__dark"></span><span class="divider__light"></span></div>
    <p class="store store--east">Eastbrook<br>482 Elm Parade<br>P: 03 9172 5843</p>
    <p class="email">email: kvtmarts@mailnest.example</p>
  </section>
</main>
</body>
</html>
```